Postcard Design

We need a postcard designed for an existing dental office in the community we are serving to mail out to the community to solicit new patients. We have an existing logo and website that we need our product designed around. We want the brochure to cater to families seeking a new dental office and need it to look upscale. Want the essentials to stand out. Our name, location, office hours and that we accept most insurances, and are always welcoming new pt. We want patients to know we have early morning "before work" hours to accommodate their schedules and for their convenience. They can always see the hygenist they choose and since we are a doctor owned and operated office, they will not be bounced from one doctor to another so they receive consistent care. To assist you , I am providing our website address. The address is brookvalefamilydentalcare.example
Thank you!
Updates

Sent this feedback to one individual but I thought I would send to all as I know alot are looking to our website for direction. Alot of these are really looking great. Some feedback.... probably best to say "teeth whitening" only on mailer as we no longer use GLIMR(even though our website still says we do. Sorry.) That way if we change whitening systems, mailer is still accurate. Also perhaps emphasize that we have convenient early morning "before work" hours and/or perhaps to highlight and put in the Clearvexa logo instead of just in small print. Also I would not post that we are closed for lunch. We can let people know when they call. Keep up the good work everyone. You guys are great and have not come across one yet I have not liked. The key is to think like a patient. What would catch your eye if you were looking for a new dentist. Important to remember that people probably get a lot of these mailers every week. I know I get several to my house at least every few weeks. What will make ours stand out? Thank you everyone for all the hard work...Regards.

Reason: I am hoping to get more submissions as many respondents were not able to meet the deadline. We have also changed this to a committed payment project.

Hey everyone. In efforts to get more design options to choose from I have increased the first place budget by another $100.00! I have also increased the project deadline our another 5 days. Thanks guys!!

Industry/Entity Type

Dental

```html
<!DOCTYPE html>
<html lang="en">
<head>
<meta charset="UTF-8">
<title>Brookvale Family Dental Care – New Patient Postcard</title>
<link rel="stylesheet" href="https://fonts.googleapis.com/css2?family=Josefin+Sans:wght@300;400;600;700&display=swap">
<style>
  :root {
    --teal: #1a9a97;
    --teal-dark: #137a78;
    --teal-light: #7cc8c4;
    --ink: #3d3d3d;
    --ink-soft: #5a5a5a;
    --paper: #f7f7f5;
    --backdrop: #e6e8e7;
    --photo-warm: #c9a98a;
    --photo-cool: #a9bfcf;
  }
  * { box-sizing: border-box; margin: 0; padding: 0; }
  html, body {
    width: 1200px; height: 800px; overflow: hidden;
    background: var(--backdrop);
    font-family: "Josefin Sans", "Century Gothic", sans-serif;
    color: var(--ink);
  }
  .spread {
    position: absolute; inset: 0;
    display: flex; align-items: center; justify-content: center; gap: 40px;
  }
  .postcard {
    position: relative;
    width: 560px; height: 373px;
    background: var(--paper);
    box-shadow: 0 6px 18px rgba(0,0,0,.18);
    overflow: hidden;
  }

  /* ---------- Back side ---------- */
  .postcard--back .top-rule {
    position: absolute; left: 0; right: 0; top: 0; height: 8px; background: var(--teal);
  }
  .headline {
    position: absolute; top: 26px; left: 0; right: 0;
    text-align: center; color: var(--teal);
    font-weight: 600; font-size: 25px; letter-spacing: 1.6px;
  }
  .intro {
    position: absolute; left: 22px; top: 84px; width: 310px;
    font-size: 10.2px; line-height: 1.35; font-weight: 400;
  }
  .intro h2, .services h2 {
    color: var(--teal); font-weight: 400; font-size: 14px; margin-bottom: 2px;
  }
  .intro p { margin-bottom: 7px; }
  .intro ul { list-style: none; }
  .intro li::before { content: "• "; }
  .intro .highlight { color: var(--teal-dark); font-weight: 600; }
  .services {
    position: absolute; left: 338px; top: 80px; width: 210px;
  }
  .services h2 { font-size: 15px; }
  .services-cols { display: flex; gap: 18px; }
  .services ul { list-style: none; font-size: 10.5px; line-height: 1.36; }
  .services li::before { content: "• "; }
  .services ul.col-right { margin-top: -14px; }
  .insurance-label {
    position: absolute; left: 22px; top: 234px;
    color: var(--teal); font-size: 10.5px;
  }
  .insurers {
    position: absolute; left: 22px; right: 22px; top: 255px;
    display: flex; justify-content: space-between; align-items: center;
  }
  .insurer {
    display: flex; align-items: center; gap: 5px;
    font-size: 12px; font-weight: 600;
  }
  .insurer .dot { width: 10px; height: 10px; border-radius: 50%; }
  .insurer--a { color: #2a6fb5; } .insurer--a .dot { background: #2a6fb5; }
  .insurer--b { color: var(--teal-dark); } .insurer--b .dot { background: var(--teal-dark); border-radius: 0; }
  .insurer--c { color: #222; }
  .insurer--d { color: #333; }
  .insurer--e { color: #1b67b3; }
  .contact {
    position: absolute; left: 22px; top: 294px;
    font-size: 10.5px; line-height: 1.38; color: var(--ink-soft); font-style: normal;
  }
  .contact-row { display: flex; align-items: center; gap: 6px; }
  .contact-row svg { width: 10px; height: 10px; fill: var(--ink); flex: none; }
  .contact-row.indent { padding-left: 16px; }
  .hours {
    position: absolute; left: 340px; top: 300px;
    font-size: 10.5px; line-height: 1.38; color: var(--ink-soft);
  }
  .hours h3 { color: var(--teal); font-weight: 400; font-size: 11px; }
  .hours .early { color: var(--teal-dark); font-weight: 600; }

  /* ---------- Front side ---------- */
  .postcard--front .swoosh { position: absolute; inset: 0; }
  .brand {
    position: absolute; top: 28px; right: 40px;
    display: flex; align-items: center; gap: 10px;
  }
  .brand .mark { width: 26px; height: 26px; border-radius: 50%; background: var(--teal); }
  .brand-name {
    font-size: 30px; font-weight: 600; letter-spacing: 2px; color: #4a4a4a; line-height: 1;
  }
  .brand-sub {
    font-size: 13px; font-weight: 600; letter-spacing: 2.5px; color: #4a4a4a; margin-top: 4px;
  }
  .hero-photo {
    position: absolute; left: 0; right: 0; bottom: 0; height: 245px;
    background: linear-gradient(135deg, var(--photo-warm) 0%, #e3cdb4 45%, var(--photo-cool) 100%);
    clip-path: path("M0 40 C 180 15, 380 8, 560 0 L560 245 L0 245 Z");
  }
</style>
</head>
<body>
<main class="spread">

  <section class="postcard postcard--back" aria-label="Postcard back">
    <div class="top-rule"></div>
    <h1 class="headline">NOW ACCEPTING NEW PATIENTS!</h1>

    <div class="intro">
      <h2>Advanced Treatments</h2>
      <p>Brookvale Family Dental Care pride themselves on providing advanced dental treatments and services to the community of Brookvale. Learn more about all the services offered through our patient education videos.</p>
      <ul>
        <li>Smile Confidently! - Invisible braces through Clearvexa</li>
        <li>Brighter Smile! - Affordable and Effective Teeth Whitening</li>
        <li class="highlight">Always see the hygienist you choose</li>
        <li class="highlight">Doctor owned &amp; operated - consistent care</li>
      </ul>
    </div>

    <div class="services">
      <h2>Our services</h2>
      <div class="services-cols">
        <ul class="col-left">
          <li>Bridges</li><li>Crowns</li><li>Dentures</li><li>Digital X-rays</li>
          <li>Fillings</li><li>Hygiene</li><li>Whitening</li>
        </ul>
        <ul class="col-right">
          <li>Implants</li><li>Inlays</li><li>Orthodontics</li><li>Perio</li>
          <li>Root canal</li><li>Veneers</li>
        </ul>
      </div>
    </div>

    <p class="insurance-label">We accept most insurance plans including:</p>
    <div class="insurers">
      <span class="insurer insurer--a"><span class="dot"></span>Veritan</span>
      <span class="insurer insurer--b"><span class="dot"></span>Corvella</span>
      <span class="insurer insurer--c">MERIDIAN DENTAL</span>
      <span class="insurer insurer--d">SENTRIX</span>
      <span class="insurer insurer--e">LifeHarbor</span>
    </div>

    <address class="contact">
      <div class="contact-row">
        <svg viewBox="0 0 10 10" aria-hidden="true"><path d="M5 0a3.5 3.5 0 0 0-3.5 3.5C1.5 6 5 10 5 10s3.5-4 3.5-6.5A3.5 3.5 0 0 0 5 0zm0 5a1.5 1.5 0 1 1 0-3 1.5 1.5 0 0 1 0 3z"/></svg>
        48B W. Larchmont Ave.
      </div>
      <div class="contact-row indent">Brookvale, FL 33900</div>
      <div class="contact-row">
        <svg viewBox="0 0 10 10" aria-hidden="true"><path d="M2 1h2l1 2.2-1.2.9a5.5 5.5 0 0 0 2.1 2.1l.9-1.2L9 6v2a1 1 0 0 1-1 1C4.1 9 1 5.9 1 2a1 1 0 0 1 1-1z"/></svg>
        (813) 555-0149
      </div>
      <div class="contact-row">
        <svg viewBox="0 0 10 10" aria-hidden="true"><path d="M2.5 0h5v3h-5zM0 3.5h10v4H8V6H2v1.5H0zM2.5 6.5h5V10h-5z"/></svg>
        (813) 555-0187
      </div>
    </address>

    <div class="hours">
      <h3>OFFICE HOURS</h3>
      <p>MON - THU &nbsp;7:00 am - 4:00 pm</p>
      <p class="early">Early morning “before work” hours!</p>
    </div>
  </section>

  <section class="postcard postcard--front" aria-label="Postcard front">
    <div class="hero-photo" role="img" aria-label="Photo of a smiling father carrying his young son on his back outdoors"></div>
    <svg class="swoosh" viewBox="0 0 560 373" aria-hidden="true">
      <path d="M0 18 C 120 40, 160 70, 150 96 C 260 96, 420 100, 560 92" fill="none" stroke="var(--teal-light)" stroke-width="1.5"/>
      <path d="M0 28 C 110 48, 150 78, 140 104 C 260 104, 420 108, 560 100" fill="none" stroke="var(--teal)" stroke-width="3"/>
    </svg>
    <div class="brand">
      <span class="mark" aria-hidden="true"></span>
      <div>
        <div class="brand-name">BROOKVALE</div>
        <div class="brand-sub">FAMILY DENTAL CARE</div>
      </div>
    </div>
  </section>

</main>
</body>
</html>
```